Property investor needs a business card with logo

I need a business card for a UK based business called 'Bright Gate Homes'. I buy houses quickly that is either hard to sell or people have been having trouble to sell. I then create the opportunity for people to buy houses that normally can't. This could be because they have little or no deposit saved up or they don't qualify for a mortgage. The design is to be bright so that it stands out but non threatening and basic. Yellow for the bass colour. The logo to be very simple and represent a house. It could include words like "cant sell? I'll buy it!!" or "Need a quick sale? Let me help" or something as simple as "I buy houses!!" The final design should communicate that I am not some big corporate person that is better that them, but someone that is just a person trying to help them with their situation. with a picture of me with the background removed.
Target Market(s)
Normal everyday people
Industry/Entity Type
Business
Contact Information for Business Card
Gareth Pellingham
07845619027
brightgatehomes@mailbox.example
Font styles to use
Other font styles liked:
- something that looks hand written
Look and feel
Each slider illustrates characteristics of the customer's brand and the style your logo design should communicate.

```html
<!DOCTYPE html>
<html lang="en">
<head>
<meta charset="utf-8">
<title>Bright Gate Homes – Business Card</title>
<link href="https://fonts.googleapis.com/css2?family=Kalam:wght@400&family=Comic+Neue:wght@400;700&display=swap" rel="stylesheet">
<style>
  :root {
    --board-light: #b9babd;
    --board-mid: #6d6e71;
    --board-dark: #414143;
    --card-yellow: #f5ed23;
    --card-white: #ffffff;
    --brand-olive: #a8a032;
    --photo-tone-a: #dfe0e2;
    --photo-tone-b: #3a3d44;
  }
  html, body {
    margin: 0;
    padding: 0;
    width: 1200px;
    height: 1000px;
    overflow: hidden;
  }
  .board {
    position: relative;
    width: 1200px;
    height: 1000px;
    background: linear-gradient(135deg, var(--board-light) 0%, var(--board-mid) 45%, var(--board-dark) 100%);
    font-family: "Comic Neue", "Comic Sans MS", cursive;
    color: var(--brand-olive);
  }
  .card {
    position: absolute;
    width: 675px;
    height: 365px;
    border-radius: 22px;
    overflow: hidden;
    background: var(--card-yellow);
  }
  .card--front { left: 123px; top: 88px; }
  .card--back { left: 122px; top: 547px; }

  .front__top {
    position: absolute;
    left: 0; top: 0;
    width: 100%;
    height: 210px;
    background: var(--card-white);
  }
  .front__logo-panel {
    position: absolute;
    left: 390px;
    top: 0;
    width: 223px;
    height: 287px;
    background: var(--card-white);
  }
  .photo-frame {
    position: absolute;
    left: 63px;
    top: 29px;
    width: 222px;
    height: 181px;
    background: var(--card-yellow);
  }
  .photo {
    position: absolute;
    left: 13px;
    top: 12px;
    width: 196px;
    height: 146px;
    background: linear-gradient(180deg, var(--photo-tone-a) 0%, var(--photo-tone-a) 45%, var(--photo-tone-b) 100%);
  }

  .contact {
    position: absolute;
    left: 20px;
    top: 227px;
    width: 310px;
    text-align: center;
    font-size: 19px;
    letter-spacing: 0.8px;
    line-height: 32px;
  }
  .contact__name { font-weight: 700; font-size: 20px; }
  .contact__email { font-size: 17px; }

  .brand {
    position: absolute;
    text-align: center;
    transform: translateX(-50%);
    white-space: nowrap;
  }
  .brand__mark {
    display: block;
    margin: 0 auto;
    background: var(--brand-olive);
  }
  .brand__name {
    display: block;
    font-family: "Kalam", cursive;
    font-weight: 400;
    color: var(--brand-olive);
  }
  .brand__tagline {
    display: block;
    font-family: "Comic Neue", "Comic Sans MS", cursive;
    color: var(--brand-olive);
  }

  .brand--front { left: 502px; top: 110px; }
  .brand--front .brand__mark { width: 80px; height: 80px; margin-bottom: 26px; }
  .brand--front .brand__name { font-size: 17px; line-height: 22px; }
  .brand--front .brand__tagline { font-size: 10px; letter-spacing: 3px; line-height: 14px; }

  .brand--back { left: 338px; top: 60px; }
  .brand--back .brand__mark { width: 150px; height: 150px; margin-bottom: 46px; }
  .brand--back .brand__name { font-size: 30px; line-height: 38px; }
  .brand--back .brand__tagline { font-size: 14px; letter-spacing: 6px; line-height: 18px; margin-top: 4px; }

  .brand--board { left: 994px; top: 320px; }
  .brand--board .brand__mark { width: 180px; height: 180px; margin-bottom: 53px; }
  .brand--board .brand__name { font-size: 36px; line-height: 44px; }
  .brand--board .brand__tagline { font-size: 16px; letter-spacing: 7px; line-height: 20px; margin-top: 6px; }
</style>
</head>
<body>
<main class="board">

  <section class="card card--front" aria-label="Business card front">
    <div class="front__top"></div>
    <div class="front__logo-panel"></div>
    <div class="photo-frame">
      <div class="photo" role="img" aria-label="Portrait photo of Gareth Pellingham with background removed"></div>
    </div>
    <div class="contact">
      <div class="contact__name">Gareth Pellingham</div>
      <div class="contact__phone">07845619027</div>
      <div class="contact__email">brightgatehomes@mailbox.example</div>
    </div>
    <div class="brand brand--front">
      <span class="brand__mark"></span>
      <span class="brand__name">Bright Gate Homes</span>
      <span class="brand__tagline">I buy houses!!</span>
    </div>
  </section>

  <section class="card card--back" aria-label="Business card back">
    <div class="brand brand--back">
      <span class="brand__mark"></span>
      <span class="brand__name">Bright Gate Homes</span>
      <span class="brand__tagline">I buy houses!!</span>
    </div>
  </section>

  <div class="brand brand--board">
    <span class="brand__mark"></span>
    <span class="brand__name">Bright Gate Homes</span>
    <span class="brand__tagline">I buy houses!!</span>
  </div>

</main>
</body>
</html>
```